Career development coaching - school lever to adults, needs a business card

Tandel Grove - An independent Career Advice business that provides 1-2-1 advice,for career development, entrepreneurial support and workshops needs a business card. Our clients of all ages (school leaver to adults looking for a career move) and universities and colleges. We would like the card to be double-sided with a modern, professional look. Looking for something professional yet very creative and original. Want a standard size business card that inspires a second look because it stands out from the rest.

One side of the card to have a design incorporating the logo with Tandel Grove name with the strap line “Helping you find your future” and space for the company website

Other side of the card to the logo/Tandel Grove name and the usual contact information:
Individual Name
Job Title (for example, Director)
Phone number
Email address
Company website address

Facebook, LinkedIn and Twitter links will need to go somewhere (back or front!)

The design will be used for 3 individuals so should be editable so that we can update as needed/as we grow.

Attached is the company logo/colours to be incorporated.

Target Market(s)

1-2-1 advice,for career development, entrepreneurial support and workshops needs a business card. Our clients of all ages (school leaver to adults looking for a career move) and universities and colleges.

Industry/Entity Type

Consulting

Contact Information for Business Card

Individual Name
Phone number
Email address
Company website address

Font styles to use
Sans Serif

Colors
0255a3
3176b5
faa54b
f78f20
85acd3
cfdeed

Requirements
Must have
• use the Tandel Grove Logo in some way - using the colours and the blue/orange palette
• For the logo - hope this makes sense to someone or if they direclty relate to the logo image attached!
• For the Orange:- Pantone 1585 C
• In CMYK : C3 M71 Y100 K0
• For the Blue:- 100% Pantone 7469 C
• In CMYK : C100 M62 Y27 K7
• Please feel free to contact me with any questions for more info
Nice to have
• happy to see any creative designs
Should not have
• Nothing too traditional,

```html
<!DOCTYPE html>
<html lang="en">
<head>
<meta charset="utf-8">
<title>Tandel Grove — Business Card</title>
<link rel="stylesheet" href="https://fonts.googleapis.com/css2?family=Questrial&family=Open+Sans:wght@400;600;700&display=swap">
<style>
  :root {
    --brand-blue: #11638f;
    --brand-blue-deep: #0e5a84;
    --brand-orange: #ef7233;
    --card-white: #ffffff;
    --backdrop: #eceef1;
    --ink-white: #ffffff;
  }
  * { margin: 0; padding: 0; box-sizing: border-box; }
  html, body { width: 1200px; height: 900px; overflow: hidden; }
  body {
    background: var(--backdrop);
    position: relative;
    font-family: "Open Sans", Arial, sans-serif;
  }
  .card {
    position: absolute;
    width: 600px;
    height: 343px;
    overflow: hidden;
    box-shadow: 0 6px 18px rgba(0,0,0,0.12);
  }
  /* Front side */
  .card-front {
    left: 470px;
    top: 80px;
    background: var(--brand-blue);
    color: var(--ink-white);
  }
  .front-name {
    position: absolute;
    left: 70px;
    top: 112px;
    font-family: "Questrial", Arial, sans-serif;
    font-size: 54px;
    font-weight: 400;
    letter-spacing: 3px;
    text-transform: uppercase;
    white-space: nowrap;
  }
  .front-tagline {
    position: absolute;
    left: 78px;
    top: 192px;
    font-size: 19px;
    font-weight: 700;
  }
  /* Back side */
  .card-back {
    left: 130px;
    top: 460px;
    background: var(--card-white);
  }
  .back-shapes { position: absolute; inset: 0; }
  .person {
    position: absolute;
    left: 72px;
    top: 22px;
  }
  .person-name {
    color: var(--brand-blue-deep);
    font-weight: 700;
    font-size: 20px;
    line-height: 1.15;
  }
  .person-title {
    color: var(--brand-orange);
    font-size: 15px;
  }
  .contact-list {
    position: absolute;
    left: 34px;
    top: 94px;
    list-style: none;
  }
  .contact-list li {
    display: flex;
    align-items: center;
    gap: 10px;
    color: var(--brand-orange);
    font-size: 17px;
    line-height: 23px;
  }
  .contact-icon { width: 14px; height: 14px; flex: none; }
  .brand-mark {
    position: absolute;
    left: 330px;
    top: 92px;
    width: 240px;
    display: flex;
    flex-direction: column;
    align-items: center;
    gap: 14px;
  }
  .brand-dot {
    width: 64px; height: 64px;
    border-radius: 50%;
    background: var(--brand-orange);
  }
  .brand-name {
    font-family: "Questrial", Arial, sans-serif;
    font-size: 27px;
    letter-spacing: 2px;
    text-transform: uppercase;
    color: var(--brand-blue-deep);
    white-space: nowrap;
  }
</style>
</head>
<body>

  <section class="card card-front" aria-label="Card front">
    <h1 class="front-name">Tandel Grove</h1>
    <p class="front-tagline">Helping You Find Your Future</p>
  </section>

  <section class="card card-back" aria-label="Card back">
    <svg class="back-shapes" width="600" height="343" viewBox="0 0 600 343" aria-hidden="true">
      <polygon points="18,22 60,22 60,52 18,52" fill="var(--brand-blue-deep)"/>
      <polygon points="40,22 60,22 60,52 18,52" fill="var(--brand-orange)"/>
      <polygon points="0,246 10,240 292,314 282,343 0,343" fill="var(--brand-blue-deep)"/>
      <polygon points="304,314 600,314 600,343 294,343" fill="var(--brand-orange)"/>
    </svg>

    <div class="person">
      <p class="person-name">Marcus Ellery</p>
      <p class="person-title">Managing Director</p>
    </div>

    <ul class="contact-list">
      <li>
        <svg class="contact-icon" viewBox="0 0 14 14" aria-hidden="true"><path d="M3 1 L5.5 4 L4 5.5 Q5.5 8.5 8.5 10 L10 8.5 L13 11 L11 13 Q4 12 1 3 Z" fill="var(--brand-blue-deep)"/></svg>
        044-987 654 321
      </li>
      <li>
        <svg class="contact-icon" viewBox="0 0 14 14" aria-hidden="true"><rect x="1" y="3" width="12" height="8" fill="var(--brand-blue-deep)"/><path d="M1 3 L7 8 L13 3" stroke="#fff" stroke-width="1" fill="none"/></svg>
        hello@tandelgrove.com
      </li>
      <li>
        <svg class="contact-icon" viewBox="0 0 14 14" aria-hidden="true"><circle cx="7" cy="7" r="6" fill="var(--brand-blue-deep)"/><path d="M1 7 H13 M7 1 Q3 7 7 13 Q11 7 7 1" stroke="#fff" stroke-width="0.8" fill="none"/></svg>
        www.tandelgrove.com
      </li>
      <li>
        <svg class="contact-icon" viewBox="0 0 14 14" aria-hidden="true"><circle cx="7" cy="7" r="7" fill="var(--brand-blue-deep)"/></svg>
        friendsnet.com/tandelgrove
      </li>
      <li>
        <svg class="contact-icon" viewBox="0 0 14 14" aria-hidden="true"><circle cx="7" cy="7" r="7" fill="var(--brand-blue-deep)"/></svg>
        proflink.com/tandelgrove
      </li>
      <li>
        <svg class="contact-icon" viewBox="0 0 14 14" aria-hidden="true"><circle cx="7" cy="7" r="7" fill="var(--brand-blue-deep)"/></svg>
        chirpline.com/tandelgrove
      </li>
    </ul>

    <div class="brand-mark">
      <span class="brand-dot" aria-hidden="true"></span>
      <span class="brand-name">Tandel Grove</span>
    </div>
  </section>

</body>
</html>
```